Online Certificate in Research Methods needs a Digital Banner ad

We are launching an online graduate certificate in Quantitative and Qualitative Social Science Research Methods. We need a digital banner created so we can advertise on pagenook, seekora, and some other places.

The banner needs to use these color schemes and fonts: https://universityrelations.bmlu.edu/brand-guide/color

Would like the banner to say (either as three lines, or if not in three lines, have these sets of words at minimum on the same line):
Online Graduate Certificate in
Quantitative & Qualitative
Social Science Research Methods

We also want it to say Brennmoor Lake University and Next Start Date August 18, 2021. I’ve attached a picture of a version we tried to create but is hard to read.

We need a graphic that looks good in the following specs:
600px wide x 70px tall, high quality (at least 300 dpi) jpg or png

And
Pagenook recommendations:
Design Recommendations
• File Type: JPG or PNG
• Ratio: 1.91:1 to 1:1
• Resolution: At least 1080 x 1080 pixels
Text Recommendations
• Primary Text: 125 characters
• Headline: 40 characters
• Description: 30 characters
Technical Requirements
• Maximum File Size: 30MB
• Minimum Width: 600 pixels
• Minimum Height: 600 pixels
• Aspect Ratio Tolerance: 3%

```html
<!DOCTYPE html>
<html lang="en">
<head>
<meta charset="utf-8">
<title>Research Methods Certificate – Banner Set</title>
<link rel="stylesheet" href="https://fonts.googleapis.com/css2?family=Rubik:ital,wght@0,800;1,900&family=Quicksand:wght@500&family=Libre+Baskerville&display=swap">
<style>
  :root {
    --navy: #002855;
    --navy-deep: #00234b;
    --gold: #eaaa00;
    --white: #ffffff;
    --page: #ffffff;
    --label: #1c3560;
    --photo-light: #ece7df;
    --photo-mid: #d8c3a6;
    --photo-warm: #b98a62;
  }
  * { box-sizing: border-box; margin: 0; padding: 0; }
  html, body { width: 1200px; height: 1000px; overflow: hidden; background: var(--page); }
  .canvas { position: relative; width: 1200px; height: 1000px; }

  .size-label {
    position: absolute;
    font-family: "Quicksand", sans-serif;
    font-weight: 500;
    font-size: 16px;
    color: var(--label);
    text-align: center;
    line-height: 21px;
    letter-spacing: 0.5px;
  }

  .banner { position: absolute; background: var(--navy); overflow: hidden; }

  .headline {
    position: absolute;
    font-family: "Rubik", sans-serif;
    font-weight: 800;
    color: var(--white);
    text-transform: uppercase;
    white-space: nowrap;
    letter-spacing: -0.2px;
  }
  .headline span { display: block; }

  .accent-slash { position: absolute; }

  .photo-area {
    position: absolute;
    background: linear-gradient(100deg, var(--photo-light) 0%, var(--photo-mid) 45%, var(--photo-warm) 75%, var(--photo-light) 100%);
  }

  .rule { position: absolute; left: 0; right: 0; }

  .wordmark {
    position: absolute;
    font-family: "Rubik", sans-serif;
    font-weight: 800;
    color: var(--white);
    white-space: nowrap;
    text-align: center;
    transform: translateX(-50%);
  }

  .date-lockup { position: absolute; overflow: visible; }
  .date-lockup text {
    font-family: "Rubik", sans-serif;
    font-style: italic;
    font-weight: 900;
    text-anchor: middle;
  }
  .date-lockup .halo { fill: var(--white); stroke: var(--white); stroke-linejoin: round; }
  .date-lockup .kicker { fill: var(--navy); stroke: var(--navy-deep); }
  .date-lockup .date { fill: var(--gold); stroke: var(--navy-deep); stroke-width: 1.4; paint-order: stroke; }
</style>
</head>
<body>
<main class="canvas">

  <!-- Leaderboard strip 600 x 70 -->
  <div class="size-label" style="left:500px; top:166px; width:200px;">600px x 70px</div>

  <section class="banner banner--strip" style="left:28px; top:198px; width:1143px; height:134px;">
    <div class="photo-area" role="img" aria-label="Photo of a young woman waving at her laptop during a video call in a bright living room"
         style="left:771px; top:0; width:372px; height:134px; clip-path:polygon(43px 0,372px 0,372px 134px,0 134px);"></div>
    <svg class="edge-lines" width="1143" height="134" style="position:absolute;left:0;top:0;">
      <polygon points="810,0 818,0 775,134 767,134" fill="#ffffff"/>
      <polygon points="816,0 821,0 778,134 773,134" fill="#eaaa00"/>
    </svg>

    <svg class="date-lockup" style="left:27px; top:28px;" width="216" height="66" viewBox="0 0 216 66">
      <text class="halo" x="108" y="20" font-size="21" textLength="176" lengthAdjust="spacingAndGlyphs" stroke-width="4">NEXT START DATE</text>
      <text class="kicker" x="108" y="20" font-size="21" textLength="176" lengthAdjust="spacingAndGlyphs" stroke-width="0.6">NEXT START DATE</text>
      <text class="halo" x="108" y="55" font-size="29" textLength="211" lengthAdjust="spacingAndGlyphs" stroke-width="5">AUGUST 18, 2021</text>
      <text class="date" x="108" y="55" font-size="29" textLength="211" lengthAdjust="spacingAndGlyphs">AUGUST 18, 2021</text>
    </svg>
    <div class="wordmark" style="left:135px; top:105px; font-size:11px;">Brennmoor Lake University</div>

    <svg class="accent-slash" style="left:248px; top:22px;" width="44" height="92" viewBox="0 0 44 92">
      <polygon points="30,0 44,0 14,92 0,92" fill="#eaaa00"/>
    </svg>
    <h1 class="headline" style="left:278px; top:31px; font-size:22.5px; line-height:24px;">
      <span>Online Graduate Certificate</span>
      <span>in Quantitative &amp; Qualitative</span>
      <span>Social Science Research Methods</span>
    </h1>
  </section>

  <!-- Square 1080 x 1080 -->
  <section class="banner banner--square" style="left:28px; top:358px; width:442px; height:442px;">
    <svg class="accent-slash" style="left:13px; top:16px;" width="36" height="75" viewBox="0 0 36 75">
      <polygon points="24,0 36,0 12,75 0,75" fill="#eaaa00"/>
    </svg>
    <h2 class="headline" style="left:37px; top:23px; font-size:19px; line-height:19.5px;">
      <span>Online Graduate Certificate</span>
      <span>in Quantitative &amp; Qualitative</span>
      <span>Social Science Research Methods</span>
    </h2>
    <div class="rule" style="top:104px; height:3px; background:var(--white);"></div>
    <div class="rule" style="top:108px; height:3px; background:var(--gold);"></div>
    <div class="photo-area" role="img" aria-label="Photo of a young woman waving at her laptop during a video call in a bright living room"
         style="left:0; top:111px; width:442px; height:202px;"></div>
    <div class="rule" style="top:313px; height:2px; background:var(--gold);"></div>
    <div class="rule" style="top:317px; height:2px; background:var(--white);"></div>

    <svg class="date-lockup" style="left:61px; top:327px;" width="300" height="90" viewBox="0 0 300 90">
      <text class="halo" x="150" y="30" font-size="30" textLength="247" lengthAdjust="spacingAndGlyphs" stroke-width="5">NEXT START DATE</text>
      <text class="kicker" x="150" y="30" font-size="30" textLength="247" lengthAdjust="spacingAndGlyphs" stroke-width="0.8">NEXT START DATE</text>
      <text class="halo" x="150" y="73" font-size="40" textLength="300" lengthAdjust="spacingAndGlyphs" stroke-width="6">AUGUST 18, 2021</text>
      <text class="date" x="150" y="73" font-size="40" textLength="300" lengthAdjust="spacingAndGlyphs">AUGUST 18, 2021</text>
    </svg>
    <div class="wordmark" style="left:221px; top:414px; font-size:12px;">Brennmoor Lake University</div>
  </section>
  <div class="size-label" style="left:149px; top:808px; width:200px;">1 : 1<br>(1080px x 1080px)</div>

  <!-- Landscape 1080 x 566 -->
  <section class="banner banner--landscape" style="left:496px; top:358px; width:675px; height:381px;">
    <svg class="accent-slash" style="left:16px; top:14px;" width="35" height="71" viewBox="0 0 35 71">
      <polygon points="23,0 35,0 12,71 0,71" fill="#eaaa00"/>
    </svg>
    <h2 class="headline" style="left:39px; top:22px; font-size:17.5px; line-height:18px;">
      <span>Online Graduate Certificate</span>
      <span>in Quantitative &amp; Qualitative</span>
      <span>Social Science Research Methods</span>
    </h2>

    <svg class="date-lockup" style="left:451px; top:20px;" width="202" height="56" viewBox="0 0 202 56">
      <text class="halo" x="101" y="20" font-size="20" textLength="168" lengthAdjust="spacingAndGlyphs" stroke-width="4">NEXT START DATE</text>
      <text class="kicker" x="101" y="20" font-size="20" textLength="168" lengthAdjust="spacingAndGlyphs" stroke-width="0.6">NEXT START DATE</text>
      <text class="halo" x="101" y="50" font-size="27" textLength="202" lengthAdjust="spacingAndGlyphs" stroke-width="5">AUGUST 18, 2021</text>
      <text class="date" x="101" y="50" font-size="27" textLength="202" lengthAdjust="spacingAndGlyphs">AUGUST 18, 2021</text>
    </svg>

    <div class="rule" style="top:99px; height:3px; background:var(--white);"></div>
    <div class="rule" style="top:106px; height:3px; background:var(--gold);"></div>
    <div class="photo-area" role="img" aria-label="Photo of a young woman waving at her laptop during a video call in a bright living room"
         style="left:0; top:110px; width:675px; height:226px;"></div>
    <div class="rule" style="top:336px; height:3px; background:var(--gold);"></div>
    <div class="rule" style="top:341px; height:3px; background:var(--white);"></div>
    <div class="wordmark" style="left:338px; top:355px; font-size:12px;">Brennmoor Lake University</div>
  </section>
  <div class="size-label" style="left:733px; top:747px; width:200px;">1.91 : 1<br>(1080px x 566px)</div>

</main>
</body>
</html>
```